Northfield Stride Sales Sheet

Please take the Microsoft Word document "Northfield Stride" that has the text and transform it into something like a cut sheet/info sheet. I've included logo package, the copy we want, and a sample cut sheet from another designer we use at times so it feels like whatever you create is in the family. Ideally we'd like to put this in front of people we're meeting at other events/engagements. It doesn't need to introduce Pembrook - just give the dressed up version of this Doc. We need to be able to print it in office on LaserJets - not take to a professional printer.

Target Market(s)

35-50 year old professional.

Industry/Entity Type

Management Consulting

Requirements
Must have
• Readability & Easy to access visually.
• Pembro logo & Style guide provided. I realize it's not as fun & we're open to some creative progress... but we want it to look like other pieces.

```html
<!DOCTYPE html>
<html lang="en">
<head>
<meta charset="utf-8">
<title>Northfield Stride Overview</title>
<link href="https://fonts.googleapis.com/css2?family=Roboto:wght@300;400;500;700&display=swap" rel="stylesheet">
<style>
:root{
  --blue:#2a5d98;
  --orange:#ec7442;
  --orange-deep:#e0622f;
  --teal:#5fb5a8;
  --ink:#222;
  --body:#555;
  --paper:#f4f4f5;
  --stage:#e9ecef;
  --white:#fff;
}
*{box-sizing:border-box;margin:0;padding:0}
html,body{width:1058px;height:1200px;overflow:hidden;background:var(--stage)}
body{font-family:'Roboto',Arial,sans-serif}
.sheet{position:absolute;left:64px;top:0;width:930px;height:1200px;display:flex}
.main{position:relative;width:596px;height:1200px;background:linear-gradient(160deg,#fafafa 0%,var(--paper) 60%,#e9e9ea 100%);color:var(--body)}
.ribbon{position:absolute;left:0;top:0}
.ribbon-label{position:absolute;left:16px;top:230px;transform:rotate(-90deg);transform-origin:left top;color:var(--white);font-size:23px;font-weight:400;letter-spacing:.5px;white-space:nowrap}
.site-mark{position:absolute;left:30px;top:1143px;transform:rotate(-90deg);transform-origin:left top;color:#dcdcdd;font-size:30px;font-weight:300;white-space:nowrap}
.block{position:absolute;left:98px;width:446px}
.title{top:52px;font-size:35px;font-weight:400;line-height:41px;color:var(--blue);text-transform:uppercase;letter-spacing:-.2px}
.title .accent{color:var(--orange);font-weight:500;display:block}
.heading{font-size:16.5px;font-weight:700;color:var(--ink);text-transform:uppercase;margin-bottom:10px}
.objectives{top:169px}
.objectives li{list-style:none;position:relative;padding-left:38px;font-size:13.8px;line-height:17.5px;margin-bottom:10px}
.objectives li::before{content:"";position:absolute;left:6px;top:2px;width:13px;height:13px;border:2px solid var(--orange);border-radius:50%}
.why{top:283px}
.why p{font-size:13.8px;line-height:17.8px;margin-bottom:17px}
.lead{color:var(--teal);font-weight:500;text-transform:uppercase}
.day{top:737px}
.day .intro{font-size:13.8px;line-height:17.8px;margin-bottom:9px}
.day ul{padding-left:18px}
.day li{font-size:13.8px;line-height:17.8px;color:var(--body)}
.day li::marker{color:var(--blue)}
.day .step{color:var(--orange);font-weight:500}
.aside{position:relative;width:334px;height:1200px;color:var(--white)}
.aside-bg{position:absolute;left:0;top:0}
.tagline{position:absolute;left:38px;top:55px;font-size:33px;font-weight:700;line-height:42px}
.process-title{position:absolute;left:38px;top:238px;font-size:34px;font-weight:300}
.step-item{position:absolute;left:36px;width:290px;display:flex;align-items:center;gap:18px}
.step-icon{width:70px;height:70px;border-radius:50%;background:var(--white);display:flex;align-items:center;justify-content:center;flex:none}
.step-text{font-size:16.5px;font-weight:700;line-height:21px}
.rule{position:absolute;left:126px;width:158px;height:2px;background:var(--white)}
.brand{position:absolute;left:30px;top:940px;font-size:30px;font-weight:500;letter-spacing:4px;text-transform:uppercase;display:flex;align-items:center;gap:12px}
.brand .dot{width:16px;height:16px;border-radius:50%;background:var(--white)}
.contact{position:absolute;left:30px;top:1035px;font-size:15.5px;line-height:20px}
.phone{position:absolute;left:30px;top:1093px;font-size:26px;font-weight:700}
.web{position:absolute;left:30px;top:1140px;font-size:15px}
</style>
</head>
<body>
<div class="sheet">
  <section class="main">
    <svg class="ribbon" width="60" height="312" viewBox="0 0 60 312"><polygon points="0,0 60,0 60,250 0,312" fill="var(--teal)"/></svg>
    <div class="ribbon-label">BE-DO-HAVE</div>
    <div class="site-mark">www.pembrookgroup.com</div>

    <h1 class="block title">Northfield Stride<span class="accent">Overview</span></h1>

    <div class="block objectives">
      <h2 class="heading">Objectives</h2>
      <ul>
        <li>To think about your life holistically</li>
        <li>To create a plan that moves you towards integrated success in all domains of your life</li>
      </ul>
    </div>

    <div class="block why">
      <h2 class="heading">Why do this?</h2>
      <p><span class="lead">Get intentional with your relationships.</span> There is a wealth of research about the impact our relationships have on our success and overall enjoyment of life. We want to help you map the people in your life and invite you to consider which relationships need to play a more significant role in your life, which need to be redefined, and when need to be central.</p>
      <p><span class="lead">Clarify your key roles.</span> What are the roles you play in your life? What are the roles you play at work? Use this exercise to identify the most important 4-6 roles you play during this season of your life.</p>
      <p><span class="lead">Core life domains inventory.</span> There are some very core domains of life we must tend to in order to live a life of sustainable impact. Using our grid, map what you want your future to look like in these areas, as well as what you need to do next.</p>
      <p><span class="lead">Learn from the story your life is telling.</span> Everyone has a story. The Professional Formation Exercise is meant to help structure the telling of your story in a way that may reveal themes and insights into your ongoing development.</p>
    </div>

    <div class="block day">
      <h2 class="heading">What is the day together?</h2>
      <p class="intro">Every one of these ends up being a little bit different, but in general we'll do this:</p>
      <ul>
        <li><span class="step">Check-In:</span> Just as it sounds - connect, chat, frame the day.</li>
        <li><span class="step">Complete the Formation Exercise:</span> Work through the remaining pieces of this exercise together. This can require some energy and emotion, so we start here.</li>
        <li><span class="step">Advance your Core Domains:</span> Building on the pre-work, we'll outline your future reality and practical next steps to get there.</li>
        <li><span class="step">Ensure you're Productive (in the ways you want) in your Key Roles:</span> Using your 4-6 roles, we'll map what you need to do to fulfill those roles.</li>
        <li><span class="step">Develop a Relationship Map:</span> This one is a lot of fun. We will take your list and turn it into a simple yet powerful plan to increase your life satisfaction and relationship health.</li>
        <li><span class="step">Draft an Integrated Success Plan:</span> All of your work will translate into an Integrated Success Plan. We'll make sure we've got all the ingredients for this. Additionally, we will send you home with a some Post-Work.</li>
        <li><span class="step">Set the Framework for Ongoing Work:</span> We suggest 6 follow-up coaching sessions after the Northfield Stride Onsite Day.</li>
      </ul>
    </div>
  </section>

  <aside class="aside">
    <svg class="aside-bg" width="334" height="1200" viewBox="0 0 334 1200">
      <defs>
        <radialGradient id="warm" cx="0.6" cy="0.45" r="0.8">
          <stop offset="0" stop-color="#ef8a5c"/>
          <stop offset="1" stop-color="var(--orange-deep)"/>
        </radialGradient>
      </defs>
      <polygon points="0,0 334,0 334,864 0,760" fill="url(#warm)" role="img" aria-label="Orange backdrop illustration of a person surrounded by circular target rings"/>
      <polygon points="0,760 334,862 334,888 0,770" fill="#e4e6ea"/>
      <polygon points="0,770 334,888 334,1200 0,1200" fill="var(--blue)"/>
    </svg>

    <div class="tagline">Think About<br>Your Life<br>Holistically</div>
    <div class="process-title">PROCESS</div>

    <div class="step-item" style="top:306px">
      <div class="step-icon"><svg width="38" height="34" viewBox="0 0 38 34"><rect x="2" y="2" width="34" height="22" rx="2" fill="none" stroke="var(--blue)" stroke-width="3"/><line x1="9" y1="10" x2="29" y2="10" stroke="var(--blue)" stroke-width="2.5"/><line x1="9" y1="16" x2="29" y2="16" stroke="var(--blue)" stroke-width="2.5"/><rect x="15" y="24" width="8" height="5" fill="var(--blue)"/><rect x="10" y="29" width="18" height="3" fill="var(--blue)"/></svg></div>
      <div class="step-text">Intake – web-based form to get to know you.</div>
    </div>
    <div class="rule" style="top:394px"></div>

    <div class="step-item" style="top:411px">
      <div class="step-icon"><svg width="34" height="38" viewBox="0 0 34 38"><rect x="4" y="6" width="12" height="28" fill="var(--blue)"/><rect x="18" y="2" width="12" height="30" fill="var(--blue)"/><line x1="10" y1="10" x2="10" y2="30" stroke="#fff" stroke-width="1.5"/></svg></div>
      <div class="step-text">Pre-work<br>Workbook</div>
    </div>
    <div class="rule" style="top:495px"></div>

    <div class="step-item" style="top:513px">
      <div class="step-icon"><svg width="40" height="30" viewBox="0 0 40 30"><path d="M2 8 Q11 4 19 8 V28 Q11 24 2 28 Z" fill="none" stroke="var(--blue)" stroke-width="2.5"/><path d="M21 8 Q29 4 38 8 V28 Q29 24 21 28 Z" fill="none" stroke="var(--blue)" stroke-width="2.5"/><line x1="26" y1="20" x2="38" y2="3" stroke="var(--blue)" stroke-width="3"/></svg></div>
      <div class="step-text">Onsite Day &amp;<br>Workbook</div>
    </div>
    <div class="rule" style="top:600px"></div>

    <div class="step-item" style="top:627px">
      <div class="step-icon"><svg width="32" height="38" viewBox="0 0 32 38"><rect x="3" y="2" width="22" height="32" rx="2" fill="none" stroke="var(--blue)" stroke-width="2.5"/><line x1="8" y1="10" x2="20" y2="10" stroke="var(--blue)" stroke-width="2"/><line x1="8" y1="16" x2="20" y2="16" stroke="var(--blue)" stroke-width="2"/><line x1="8" y1="22" x2="16" y2="22" stroke="var(--blue)" stroke-width="2"/><circle cx="25" cy="30" r="5" fill="var(--blue)"/></svg></div>
      <div class="step-text">Follow Up &amp;<br>Success Plan<br>Creation</div>
    </div>

    <div class="brand"><span class="dot"></span>Pembrook</div>
    <div class="contact">© 2017 Pembrook Company.<br>PO Box 418, Alder Falls,<br>MA 01999 USA</div>
    <div class="phone">555.014.0282</div>
    <div class="web">www.pembrookgroup.com/stride</div>
  </aside>
</div>
</body>
</html>
```